Tevrix BIM business website

I have a logo design and business card concept is ongoing at this point, but i need a website design based on VDC or BIM ("Virtual Building and Construction" or "Building Information Modeling") that will stand out for the quality and concept that we provide. I am a consultant providing training and production work for Quorvel (Zembrick application <where most of the overview can be obtained>). We are providing BIM production and coordination services as well. I can fill in the meat but I need an open development website. Currently, just obtaining a domain so it can be included on a business card is the quickest objective, then developing the content and launching it.

Business

```html
<!DOCTYPE html>
<html lang="en">
<head>
<meta charset="utf-8">
<title>Tevrix BIM Consulting</title>
<link rel="stylesheet" href="https://fonts.googleapis.com/css2?family=Lato:wght@300;400;700;900&family=Montserrat:wght@400;600;700&display=swap">
<style>
:root{
  --yellow:#f5b324;
  --dark:#333333;
  --darker:#282828;
  --ink:#222222;
  --muted:#8a8a8a;
  --light:#f2f2f2;
  --line:#e2e2e2;
  --white:#ffffff;
}
*{margin:0;padding:0;box-sizing:border-box}
html,body{width:1200px;height:3137px;overflow:hidden;background:var(--white)}
body{font-family:'Lato',sans-serif;color:var(--ink);position:relative}
.abs{position:absolute}
section,header,footer{position:absolute;left:0;width:1200px}

/* top bar + header */
.topbar{top:0;height:38px;background:var(--white)}
.topbar .strip{position:absolute;left:300px;top:0;width:840px;height:34px;background:#ececec;clip-path:polygon(0 0,100% 0,97% 100%,3% 100%)}
.topbar .info{position:absolute;top:10px;font-size:13px;color:#777;display:flex;align-items:center;gap:10px}
.site-header{top:38px;height:102px;background:var(--white);border-bottom:1px solid var(--line)}
.brand{position:absolute;left:84px;top:26px;display:flex;align-items:center;gap:10px}
.brand .dot{width:40px;height:40px;border-radius:50%;background:var(--dark)}
.brand .name{font-family:'Lato',sans-serif;font-weight:900;font-size:34px;color:var(--dark)}
.nav{position:absolute;top:42px;left:352px;display:flex;font-size:14px;font-weight:700;color:#666}
.nav a{position:absolute;white-space:nowrap;color:#666;text-decoration:none}
.nav .active{color:var(--ink)}
.nav .active::after{content:"";position:absolute;left:-4px;right:-4px;top:38px;height:3px;background:var(--yellow)}
.nav-sep{position:absolute;left:392px;top:20px;width:1px;height:56px;background:var(--line)}
.quote-btn{position:absolute;left:938px;top:31px;width:176px;height:57px;background:var(--yellow);color:var(--white);font-size:13px;font-weight:700;display:flex;align-items:center;justify-content:center;letter-spacing:.3px}

/* hero */
.hero{top:140px;height:415px;background:linear-gradient(100deg,#3a3b3d 0%,#55575a 45%,#6f7478 70%,#4a4c4f 100%)}
.hero h1{position:absolute;left:84px;top:106px;font-weight:400;font-size:48px;line-height:60px;color:var(--white);width:510px}
.btn{background:var(--yellow);color:var(--white);font-weight:700;display:flex;align-items:center;justify-content:center}
.hero .btn{position:absolute;left:84px;top:256px;width:132px;height:42px;font-size:15px;font-weight:400}
.dots{position:absolute;left:582px;top:378px;display:flex;gap:7px}
.dots i{width:6px;height:6px;border-radius:50%;background:rgba(255,255,255,.5)}
.dots i.on{background:var(--white)}

/* what we do */
.what{top:555px;height:613px;background:var(--white)}
.section-title{font-weight:700;font-size:24px;letter-spacing:.3px}
.section-title .hl{color:var(--yellow)}
.what .bracket{position:absolute;left:105px;top:40px;width:40px;height:32px;border-left:3px solid var(--yellow);border-bottom:3px solid var(--yellow)}
.what .section-title{position:absolute;left:126px;top:40px}
.tabs{position:absolute;left:664px;top:40px;width:429px;height:46px;border-bottom:1px solid var(--line);display:flex;font-family:'Montserrat',sans-serif;font-size:11px;font-weight:600;color:#999}
.tabs span{display:flex;align-items:center;justify-content:center;padding:0 20px}
.tabs .on{color:var(--yellow);border:1px solid var(--line);border-bottom:1px solid var(--white);background:var(--white);margin-bottom:-1px}
.what h3{position:absolute;left:106px;top:128px;font-size:18px;font-weight:700}
.what p.lead{position:absolute;left:106px;top:170px;width:420px;font-family:'Montserrat',sans-serif;font-size:12px;line-height:23px;color:#b0b0b0}
.stat{position:absolute;left:106px;top:341px;width:420px;height:59px;border-top:1px solid var(--line);border-bottom:1px solid var(--line)}
.stat .num{position:absolute;left:0;top:10px;font-family:'Montserrat',sans-serif;font-size:36px;font-weight:700;color:var(--yellow);line-height:40px}
.stat .bar{position:absolute;left:77px;top:16px;width:3px;height:30px;background:var(--ink)}
.stat .lbl{position:absolute;left:86px;top:31px;font-family:'Montserrat',sans-serif;font-size:10px;font-weight:700}
.stat .see{position:absolute;right:0;top:27px;font-family:'Montserrat',sans-serif;font-size:11px;font-weight:700;color:var(--yellow)}
.what h4{position:absolute;left:106px;top:441px;font-size:18px;font-weight:700}
.steps{position:absolute;left:106px;top:485px;width:420px;height:70px;font-family:'Montserrat',sans-serif}
.steps .big{position:absolute;top:-4px;font-size:64px;font-weight:700;color:#f1f1f1;line-height:70px}
.steps .lbl{position:absolute;top:30px;font-size:11px;font-weight:700;white-space:nowrap}
.steps svg{position:absolute;top:30px}
.what .photo{position:absolute;left:611px;top:132px;width:480px;height:419px;background:linear-gradient(160deg,#cfd2d3 0%,#9ea3a3 45%,#6b6357 80%,#4d4337 100%)}

/* projects */
.projects{top:1168px;height:396px;background:var(--light)}
.filters{position:absolute;left:86px;top:40px;width:1028px;height:52px;border-bottom:1px solid var(--line);display:flex;gap:27px;font-size:13px;font-weight:700;color:#888}
.filters span{padding-top:6px;position:relative}
.filters .on{color:var(--ink)}
.filters .on::after{content:"";position:absolute;left:0;right:-10px;top:49px;height:3px;background:var(--yellow)}
.arrow-box{position:absolute;width:40px;height:40px;background:var(--white);display:flex;align-items:center;justify-content:center}
.card{position:absolute;top:120px;width:237px;height:220px;background:var(--white)}
.card .img{height:157px}
.card h5{position:absolute;left:18px;top:172px;font-size:13px;font-weight:700}
.card time{position:absolute;left:18px;top:191px;font-size:12px;color:#999}
.card .corner{position:absolute;right:8px;bottom:8px}

/* blogs */
.blogs{top:1564px;height:513px;background:var(--white)}
.blogs .section-title{position:absolute;left:0;width:1200px;text-align:center;top:40px;font-size:27px}
.post{position:absolute;top:113px;width:324px;height:351px}
.post .img{height:220px}
.post .body{position:absolute;top:233px;left:0;width:324px;height:118px;background:#efefef;border-bottom:3px solid var(--dark)}
.post h6{position:absolute;left:18px;top:20px;width:290px;font-size:12px;font-weight:700;line-height:15px}
.post .meta{position:absolute;left:18px;top:69px;width:290px;border-top:1px solid #d8d8d8;padding-top:12px;display:flex;align-items:center;gap:9px;font-size:11px;color:#777}
.post .meta i{width:8px;height:8px;border-radius:50%;background:#777}
.post .meta .sep{width:1px;height:12px;background:#999;margin:0 6px}

/* testimonials */
.testimonials{top:2077px;height:373px;background:var(--light)}
.testimonials h2{position:absolute;left:90px;top:36px;font-size:27px;font-weight:700}
.quote-card{position:absolute;left:90px;top:99px;width:917px;height:209px;background:var(--white);border-left:4px solid var(--yellow)}
.quote-card .tail{position:absolute;left:56px;bottom:-32px}
.quote-card .avatar{position:absolute;left:53px;top:52px;width:96px;height:96px;background:linear-gradient(180deg,#c9b7a3,#8f7b66)}
.quote-card .who{position:absolute;left:174px;top:76px;font-size:13px;line-height:19px;color:#999}
.quote-card .who b{display:block;color:var(--ink);margin-bottom:2px}
.quote-card .who-line{position:absolute;left:174px;top:56px;width:180px;height:1px;background:var(--line)}
.quote-card p{position:absolute;left:380px;top:70px;width:500px;font-size:13.5px;line-height:22px;color:#999}
.quote-nav{position:absolute;top:99px;width:43px;height:209px;background:var(--white);display:flex;align-items:center;justify-content:center}

/* call back */
.callback{top:2450px;height:339px;background:var(--white)}
.callback .kicker{position:absolute;left:88px;top:42px;font-size:11px;color:var(--yellow)}
.callback h2{position:absolute;left:88px;top:57px;font-size:26px;font-weight:700;letter-spacing:.3px}
.callback .ask{position:absolute;left:88px;top:122px;font-size:13px;font-weight:700}
.field{position:absolute;height:38px;border:1px solid var(--line);background:#f7f7f7;font-size:13px;color:#888;padding-left:16px;display:flex;align-items:center}
.field.select{border:2px solid var(--ink);background:var(--white);color:var(--ink)}
.callback .submit{position:absolute;left:88px;top:249px;width:109px;height:38px;font-size:12px}
.consult{position:absolute;left:614px;top:124px;width:494px;height:105px;border:3px solid var(--yellow)}
.consult .small{position:absolute;left:121px;top:28px;font-size:11px;color:#888}
.consult .phone{position:absolute;left:121px;top:44px;font-family:'Montserrat',sans-serif;font-size:21px;font-weight:700;color:var(--yellow)}
.consult svg{position:absolute;left:48px;top:30px}
.hours{position:absolute;left:614px;top:251px;font-size:14px;font-weight:700}
.hours span{color:#888;font-weight:400}

/* footer */
.site-footer{top:2789px;height:293px;background:var(--dark);color:#ddd}
.foot-brand{position:absolute;left:88px;top:80px;display:flex;align-items:center;gap:12px}
.foot-brand .dot{width:48px;height:48px;border-radius:50%;background:var(--white)}
.foot-brand .name{font-weight:900;font-size:40px;color:var(--white)}
.socials{position:absolute;left:84px;top:204px;display:flex;gap:20px}
.socials i{width:33px;height:33px;border-radius:50%;background:#f0f0f0}
.col{position:absolute;top:40px}
.col h4{font-size:19px;font-weight:400;color:var(--white);margin-bottom:22px}
.col ul{list-style:none;font-size:13px;line-height:26.6px;color:#e6e6e6}
.col li::before{content:"›";display:inline-block;width:22px;color:#bbb}
.news input{display:block;width:277px;height:38px;background:#2b2b2b;border:1px solid #3d3d3d;color:#777;font-family:'Lato',sans-serif;font-size:13px;padding-left:16px;margin-bottom:19px}
.news .send{width:149px;height:31px;border-radius:16px;background:var(--yellow);color:var(--white);font-size:15px;display:flex;align-items:center;justify-content:center;margin-top:8px}
.copyright{position:absolute;left:0;top:3082px;width:1200px;height:55px;background:var(--darker);color:#ddd;font-size:13px;display:flex;align-items:center;justify-content:center}
</style>
</head>
<body>

<header class="topbar">
  <div class="strip"></div>
  <div class="info" style="left:360px">
    <svg width="13" height="13" viewBox="0 0 24 24"><path d="M6.6 10.8a15 15 0 0 0 6.6 6.6l2.2-2.2c.3-.3.7-.4 1-.2 1.1.4 2.3.6 3.6.6.6 0 1 .4 1 1V20c0 .6-.4 1-1 1C10.6 21 3 13.4 3 4c0-.6.4-1 1-1h3.5c.6 0 1 .4 1 1 0 1.3.2 2.5.6 3.6.1.3 0 .7-.2 1z" fill="#999"/></svg>
    <span>Phone number : 1-800-555-0147</span>
  </div>
  <div class="info" style="left:596px">
    <svg width="15" height="11" viewBox="0 0 15 11"><rect width="15" height="11" fill="#999"/><path d="M0 0l7.5 6L15 0" stroke="#ececec" fill="none"/></svg>
    <span>E-mail address : hello@tevrix-mail.com</span>
  </div>
  <svg class="abs" style="left:1091px;top:10px" width="16" height="15" viewBox="0 0 16 15"><circle cx="8" cy="4.5" r="4" fill="#aaa"/><path d="M0 15c0-4 3.5-6 8-6s8 2 8 6z" fill="#aaa"/></svg>
</header>

<header class="site-header">
  <div class="brand"><span class="dot"></span><span class="name">Tevrix</span></div>
  <svg class="abs" style="left:342px;top:42px" width="19" height="16" viewBox="0 0 19 16"><path d="M9.5 0L0 8h2.5v8h5v-5h4v5h5V8H19z" fill="#999"/></svg>
  <div class="nav-sep"></div>
  <nav class="nav" style="left:0">
    <a class="active" style="left:420px">Home</a>
    <a style="left:496px">About</a>
    <a style="left:571px">Services</a>
    <a style="left:662px">Projects</a>
    <a style="left:750px">News</a>
    <a style="left:823px">Contact</a>
  </nav>
  <svg class="abs" style="left:593px;top:68px" width="8" height="5" viewBox="0 0 8 5"><path d="M0 0h8L4 5z" fill="#999"/></svg>
  <div class="quote-btn">REQUEST A QUOTE</div>
</header>

<section class="hero" role="img" aria-label="Modern kitchen interior with large windows overlooking mountains">
  <h1>Lorem Ipsum is amajor key to success.</h1>
  <div class="btn">Read More</div>
  <div class="dots"><i></i><i class="on"></i><i></i></div>
</section>

<section class="what">
  <div class="bracket"></div>
  <h2 class="section-title"><span class="hl">WHAT</span> WE DO</h2>
  <div class="tabs"><span class="on">CONSULTANT</span><span>DESIGN</span><span>BUILDING</span><span>FURNITURE</span></div>
  <h3>CONSULTANT</h3>
  <p class="lead">Lorem ipsum is a major key to success. Put it this way, good models take patience, careful coordination and steady teamwork, and we are never giving up, we are just getting started. It is on you how you want to plan your build. Every project has a choice. We pick clarity, clean data and early clash checks. Let's see what the next design phase brings to the site. Plan well. Build well.</p>
  <div class="stat">
    <span class="num">500</span><span class="bar"></span><span class="lbl">PROJECTS</span>
    <span class="see">SEE ALL +</span>
  </div>
  <h4>WORK PROCESS</h4>
  <div class="steps">
    <span class="big" style="left:56px">1</span>
    <span class="big" style="left:186px">2</span>
    <span class="big" style="left:318px">3</span>
    <span class="lbl" style="left:28px">FIRST STEP</span>
    <svg style="left:142px" width="8" height="12" viewBox="0 0 8 12"><path d="M1 1l5 5-5 5" stroke="#888" stroke-width="2" fill="none"/></svg>
    <span class="lbl" style="left:160px">SECOND STEP</span>
    <svg style="left:266px" width="8" height="12" viewBox="0 0 8 12"><path d="M1 1l5 5-5 5" stroke="#888" stroke-width="2" fill="none"/></svg>
    <span class="lbl" style="left:314px">THIRD STEP</span>
  </div>
  <div class="photo" role="img" aria-label="Bright living room interior with tall windows, fireplace and wooden floor"></div>
</section>

<section class="projects">
  <div class="filters">
    <span class="on">All Projects</span><span>Interior Design</span><span>Renovation</span><span>Architecture</span><span>Landscaping</span><span>Gardening</span>
  </div>
  <div class="arrow-box" style="left:1022px;top:28px"><svg width="6" height="8" viewBox="0 0 6 8"><path d="M6 0v8L0 4z" fill="#333"/></svg></div>
  <div class="arrow-box" style="left:1072px;top:28px"><svg width="6" height="8" viewBox="0 0 6 8"><path d="M0 0v8l6-4z" fill="#333"/></svg></div>

  <article class="card" style="left:86px">
    <div class="img" role="img" aria-label="Staircase addition in a bright hall" style="background:linear-gradient(180deg,#e4e1dc,#8b7a66)"></div>
    <h5>Staircase Addition</h5><time>November 2015</time>
    <svg class="corner" width="8" height="8" viewBox="0 0 8 8"><path d="M8 0v8H0z" fill="#bbb"/></svg>
  </article>
  <article class="card" style="left:350px">
    <div class="img" role="img" aria-label="Brick townhouse facade" style="background:linear-gradient(180deg,#6e3a2c,#4b2d24)"></div>
    <h5>Townhouse Facade</h5><time>October 2015</time>
    <svg class="corner" width="8" height="8" viewBox="0 0 8 8"><path d="M8 0v8H0z" fill="#bbb"/></svg>
  </article>
  <article class="card" style="left:614px">
    <div class="img" role="img" aria-label="Family house floor plan model" style="background:linear-gradient(180deg,#f4f4f4,#c9b59a)"></div>
    <h5>Family House Plans</h5><time>November 2015</time>
    <svg class="corner" width="8" height="8" viewBox="0 0 8 8"><path d="M8 0v8H0z" fill="#bbb"/></svg>
  </article>
  <article class="card" style="left:877px">
    <div class="img" role="img" aria-label="Living room with gas chimney" style="background:linear-gradient(180deg,#d7d2cb,#555150)"></div>
    <h5>Gas Chimney Adaptation</h5><time>August 2015</time>
    <svg class="corner" width="8" height="8" viewBox="0 0 8 8"><path d="M8 0v8H0z" fill="#bbb"/></svg>
  </article>
</section>

<section class="blogs">
  <h2 class="section-title"><span class="hl">RECENT</span> BLOGS</h2>
  <article class="post" style="left:86px">
    <div class="img" role="img" aria-label="Black and white glass lattice roof" style="background:linear-gradient(180deg,#bdbdbd,#3a3a3a)"></div>
    <div class="body"><h6>Contrary to popular belief Lorem Ipsum is not simply random text</h6>
      <div class="meta"><span>Jun 25,2016</span><span class="sep"></span><i></i><i></i><i></i><i></i><i></i><i></i></div></div>
  </article>
  <article class="post" style="left:440px">
    <div class="img" role="img" aria-label="Curved steel canopy against blue sky" style="background:linear-gradient(180deg,#7aa8d6,#c7ced6)"></div>
    <div class="body"><h6>Contrary to popular belief Lorem Ipsum is not simply random text</h6>
      <div class="meta"><span>Jun 25,2016</span><span class="sep"></span><i></i><i></i><i></i><i></i><i></i><i></i></div></div>
  </article>
  <article class="post" style="left:792px">
    <div class="img" role="img" aria-label="Tower cranes over a construction site" style="background:linear-gradient(180deg,#3f7fc8,#b08a6a)"></div>
    <div class="body"><h6>Contrary to popular belief Lorem Ipsum is not simply random text</h6>
      <div class="meta"><span>Jun 25,2016</span><span class="sep"></span><i></i><i></i><i></i><i></i><i></i><i></i></div></div>
  </article>
</section>

<section class="testimonials">
  <h2>Testimonials</h2>
  <div class="quote-card">
    <svg class="tail" width="34" height="32" viewBox="0 0 34 32"><path d="M0 0h34L0 32z" fill="#fff"/></svg>
    <div class="avatar" role="img" aria-label="Portrait of the client"></div>
    <div class="who-line"></div>
    <div class="who"><b>Dan Morrow</b>Corvane Design &amp;<br>Engineering</div>
    <p>As the architect for major projects I really like to collaborte with Framewell company. We are particularly organized through the construction process. My own project was a great example of contractors and architects working as a team for the good of the project and its users.</p>
  </div>
  <div class="quote-nav" style="left:1017px"><svg width="6" height="8" viewBox="0 0 6 8"><path d="M6 0v8L0 4z" fill="#333"/></svg></div>
  <div class="quote-nav" style="left:1067px"><svg width="6" height="8" viewBox="0 0 6 8"><path d="M0 0v8l6-4z" fill="#333"/></svg></div>
</section>

<section class="callback">
  <span class="kicker">call back</span>
  <h2>REQUEST A CALL BACK</h2>
  <span class="ask">How can we help?</span>
  <div class="field select" style="left:88px;top:155px;width:234px">Business Consulting
    <svg class="abs" style="right:10px;top:14px" width="8" height="6" viewBox="0 0 8 6"><path d="M0 0h8L4 6z" fill="#222"/></svg></div>
  <div class="field" style="left:327px;top:155px;width:232px">Name</div>
  <div class="field" style="left:88px;top:199px;width:234px">Email</div>
  <div class="field" style="left:327px;top:199px;width:232px">Phone NO</div>
  <div class="btn submit">SUBMIT</div>
  <div class="consult">
    <svg width="40" height="40" viewBox="0 0 24 24"><path d="M6.6 10.8a15 15 0 0 0 6.6 6.6l2.2-2.2c.3-.3.7-.4 1-.2 1.1.4 2.3.6 3.6.6.6 0 1 .4 1 1V20c0 .6-.4 1-1 1C10.6 21 3 13.4 3 4c0-.6.4-1 1-1h3.5c.6 0 1 .4 1 1 0 1.3.2 2.5.6 3.6.1.3 0 .7-.2 1z" fill="#f5b324"/></svg>
    <span class="small">Get Free Consultation</span>
    <span class="phone">(123)- 123-45678</span>
  </div>
  <div class="hours">MONDAY - SATURDAY <span>/ 9:00 - 8:00</span></div>
</section>

<footer class="site-footer">
  <div class="foot-brand"><span class="dot"></span><span class="name">Tevrix</span></div>
  <div class="socials"><i></i><i></i><i></i><i></i></div>
  <div class="col" style="left:396px">
    <h4>Quick Links</h4>
    <ul><li>Home</li><li>About</li><li>Services</li><li>Projects</li><li>News</li><li>Contact</li></ul>
  </div>
  <div class="col" style="left:618px">
    <h4>Our Service</h4>
    <ul><li>Metal Roofing</li><li>Construction Consultant</li><li>Green Building</li><li>Laminate Flooring</li><li>House Renovation</li></ul>
  </div>
  <div class="col news" style="left:875px">
    <h4>Newsletter</h4>
    <input type="text" placeholder="Your Name">
    <input type="text" placeholder="Your Email">
    <div class="send">SEND</div>
  </div>
</footer>
<div class="copyright">© Copyrighted &nbsp;All rights reserved 2017</div>

</body>
</html>
```